Commercial Construction Company

We need a business card design based on our current logo. We are a commercial general contractor based in Southern California that specializes in bank remodels. We would like to see designs that incorporate dark blue. The final design should portray an image of professionalism and quality.

If possible, I would like to add metallic foil to the design. Thank you

```html
<!DOCTYPE html>
<html lang="en">
<head>
<meta charset="utf-8">
<title>Business Card – Front and Back</title>
<link href="https://fonts.googleapis.com/css2?family=Montserrat:wght@400;700&display=swap" rel="stylesheet">
<style>
  :root {
    --page-bg: #cdd2d6;
    --card-white: #ffffff;
    --ink-black: #0c0c0c;
    --brand-blue: #17467f;
    --brand-grey: #9d9d9d;
    --text-light: #ffffff;
    --text-dark: #1a1a1a;
  }
  * { margin: 0; padding: 0; box-sizing: border-box; }
  html, body {
    width: 1200px; height: 1200px; overflow: hidden;
    background: var(--page-bg);
    font-family: "Montserrat", sans-serif;
  }
  .card {
    position: absolute;
    width: 785px; height: 448px;
    background: var(--card-white);
    overflow: hidden;
  }
  .card--front { left: 207px; top: 92px; }
  .card--back { left: 205px; top: 558px; }

  .front-shapes { position: absolute; inset: 0; }

  .name-marker {
    position: absolute; left: 0; top: 200px;
    width: 21px; height: 50px;
    background: var(--brand-blue);
  }
  .company-name {
    position: absolute; left: 30px; top: 192px;
    color: var(--text-light);
    font-weight: 700; font-size: 30px; letter-spacing: 0.5px;
    line-height: 1;
  }
  .company-suffix {
    position: absolute; left: 30px; top: 232px;
    color: var(--text-light);
    font-weight: 400; font-size: 20px; line-height: 1;
  }
  .contact-list {
    position: absolute; left: 30px; top: 303px;
    list-style: none;
    color: var(--text-light);
    font-size: 19px; font-weight: 400;
  }
  .contact-list li {
    display: flex; align-items: center;
    height: 28.3px;
  }
  .contact-icon {
    width: 20px; height: 20px; margin-right: 10px;
    fill: #d8d8d8; flex: none;
  }
  .contact-square {
    width: 18px; height: 18px; margin: 0 11px 0 1px;
    background: #d8d8d8; border-radius: 2px; flex: none;
  }

  .brand-lockup {
    position: absolute;
    display: flex; align-items: center; gap: 14px;
  }
  .brand-lockup--front { left: 474px; top: 122px; }
  .brand-lockup--back { left: 242px; top: 200px; }
  .brand-dot {
    width: 44px; height: 44px; border-radius: 50%;
    background: var(--brand-blue);
  }
  .brand-name {
    font-weight: 700; font-size: 30px; color: var(--ink-black);
    letter-spacing: 1px;
  }
  .brand-lockup--back .brand-name { font-size: 36px; }
  .brand-lockup--back .brand-dot { width: 52px; height: 52px; }

  .address {
    position: absolute; left: 480px; top: 386px;
    display: flex; align-items: center;
    color: var(--text-dark); font-size: 19px;
  }
  .address svg { width: 20px; height: 28px; margin-right: 10px; fill: var(--brand-grey); }
</style>
</head>
<body>

<section class="card card--front">
  <svg class="front-shapes" viewBox="0 0 785 448" width="785" height="448" aria-hidden="true">
    <path d="M383 0 Q515 200 380 405 L383 405 Q497 215 358 0 Z" fill="var(--brand-blue)"/>
    <path d="M0 0 H345 Q509 224 345 448 H0 Z" fill="var(--ink-black)"/>
  </svg>

  <div class="name-marker"></div>
  <h1 class="company-name">CALDERA WORKS</h1>
  <p class="company-suffix">LDA</p>

  <ul class="contact-list">
    <li>
      <svg class="contact-icon" viewBox="0 0 24 24"><path d="M2 8c0-2 4-4 10-4s10 2 10 4v2h-5V8.5c-1.5-.6-3-.8-5-.8s-3.5.2-5 .8V10H2z M6 11h12l2 9H4z"/></svg>
      215550142
    </li>
    <li>
      <svg class="contact-icon" viewBox="0 0 24 24"><path d="M6.6 10.8a15 15 0 0 0 6.6 6.6l2.2-2.2c.3-.3.7-.4 1-.2 1.1.4 2.3.6 3.6.6.6 0 1 .4 1 1V20c0 .6-.4 1-1 1C10.6 21 3 13.4 3 4c0-.6.4-1 1-1h3.5c.6 0 1 .4 1 1 0 1.3.2 2.5.6 3.6.1.3 0 .7-.2 1z"/></svg>
      +351 215550142
    </li>
    <li>
      <svg class="contact-icon" viewBox="0 0 24 24"><path d="M2 5h20v14H2z M3.5 6.5 12 13l8.5-6.5" fill="#d8d8d8"/><path d="M3 6.5 12 13l9-6.5" stroke="#0c0c0c" stroke-width="1.6" fill="none"/></svg>
      calderaworks.mail@example.com
    </li>
    <li>
      <span class="contact-square"></span>
      www.calderaworks.com/team
    </li>
  </ul>

  <div class="brand-lockup brand-lockup--front">
    <span class="brand-dot"></span>
    <span class="brand-name">NORLAND BUILD</span>
  </div>

  <p class="address">
    <svg viewBox="0 0 20 28"><path d="M10 0a10 10 0 0 0-10 10c0 7 10 18 10 18s10-11 10-18A10 10 0 0 0 10 0zm0 14a4 4 0 1 1 0-8 4 4 0 0 1 0 8z"/></svg>
    Rua das Oliveiras, 42
  </p>
</section>

<section class="card card--back">
  <div class="brand-lockup brand-lockup--back">
    <span class="brand-dot"></span>
    <span class="brand-name">NORLAND BUILD</span>
  </div>
</section>

</body>
</html>
```